Unternehmensberatung sucht Kartendesign für Seminarspiel
Zielgruppe
Projekt: Kartenspiel Seminarspiel für Führungskräfte / Trainerbedarf
Wir sind eine Unternehmensberatung, die Führungskräfte und Unternehmen in Veränderungsprozessen begleitet.
Aufgabenstellung
Desgin: in DIN A6 als Druckvorlage bzw. zur Verwendung der Bilddateien.
ZU designen: 1 Rückseite:
ca. 9 Vorderseiten-Designs, div. Texte -> 60 Seiten
1 Verpackung

```html
<!DOCTYPE html>
<html lang="de">
<head>
<meta charset="utf-8">
<title>Seminarspiel Positive Führung – Kartenübersicht</title>
<link href="https://fonts.googleapis.com/css2?family=Arimo:wght@400;700&display=swap" rel="stylesheet">
<style>
  :root {
    --board: #737373;
    --card-blue: #3a89c9;
    --card-white: #ffffff;
    --ink: #111111;
  }
  * { margin: 0; padding: 0; box-sizing: border-box; }
  html, body { width: 1200px; height: 912px; overflow: hidden; }
  body {
    background: var(--board);
    font-family: "Arimo", Arial, sans-serif;
    position: relative;
  }
  .card {
    position: absolute;
    width: 246px;
    height: 174px;
    overflow: hidden;
  }
  .col-1 { left: 42px; }
  .col-2 { left: 339px; }
  .col-3 { left: 628px; }
  .col-4 { left: 911px; }
  .row-1 { top: 65px; }
  .row-2 { top: 257px; }
  .row-3 { top: 476px; }
  .row-4 { top: 668px; }

  .card-front { background: var(--card-white); color: var(--ink); }
  .card-front .deco { position: absolute; inset: 0; width: 246px; height: 174px; }
  .card-front .deco path, .card-front .deco rect, .card-front .deco polygon { fill: var(--card-blue); }

  .task {
    position: absolute;
    left: 17px; right: 17px; top: 18px;
    text-align: center;
    font-size: 10.4px;
    line-height: 11.9px;
  }
  .task .label { display: block; }
  .note {
    position: absolute;
    left: 18px; right: 18px; top: 123px;
    text-align: center;
    font-size: 5.6px;
    line-height: 6.5px;
  }

  .card-back {
    background: var(--card-blue);
    color: var(--card-white);
    display: flex;
    align-items: center;
    justify-content: center;
    text-align: center;
    padding-bottom: 4px;
  }
  .card-back .title {
    font-size: 23px;
    line-height: 26.5px;
    font-weight: 700;
    letter-spacing: 0.2px;
    white-space: nowrap;
  }

  /* individual tweaks */
  .strength .task { left: 12px; right: 28px; }
  .strength .note { left: 22px; right: 52px; }
  .communication .task { left: 14px; right: 14px; }
  .communication .note { left: 16px; right: 16px; }
  .culture .note { left: 14px; right: 14px; }
  .mindset .note { left: 24px; right: 22px; top: 124px; }
  .resilience .note { left: 16px; right: 16px; top: 124px; }
  .meaning .task { left: 14px; right: 14px; }
  .meaning .note { left: 16px; right: 16px; top: 124px; }
  .perma .task { left: 14px; right: 14px; top: 14px; font-size: 8.5px; line-height: 9.8px; letter-spacing: -0.1px; }
  .perma .note { left: 14px; right: 14px; top: 124px; }
</style>
</head>
<body>

  <!-- Row 1: fronts -->
  <article class="card card-front col-1 row-1 strength">
    <svg class="deco" viewBox="0 0 246 174" aria-hidden="true"><polygon points="246,0 246,174 202,174"/></svg>
    <p class="task"><span class="label">a.</span>Stärkenbrille: Fokussiere Dich in Deinen Gesprächen darauf, Deinem Gesprächspartner am Ende eine wertvolle Stärke zurückzumelden, die Dir an Ihm auffällt.</p>
    <p class="note">Sorge dafür, dass Deine Mitarbeiter bei der Arbeit das tun können, was sie am besten können! Der Stärkenfokus ist zentral im Positive Leadership-Ansatz und hat, wenn konsequent angewandt, verschiedene positive Effekte in Unternehmen wie die Steigerung der Produktivität und des Wohlbefindens des Einzelnen, die Verbesserung der Mitarbeiterbindung und der Senkung des Krankenstandes.</p>
  </article>

  <article class="card card-front col-2 row-1 trust">
    <svg class="deco" viewBox="0 0 246 174" aria-hidden="true"><path d="M0 147 Q123 175 246 147 L246 174 L0 174 Z"/></svg>
    <p class="task"><span class="label">a.</span>Offenheit: Offenheit schafft Vertrauen. Fokussiere Dich auf etwas, das Dich gerade beschäftigt. Teile Deine Gedanken mit einer Person, die diese Offenheit von Deiner Seite bislang nicht kennt.</p>
    <p class="note">Mit großem Abstand gehören im Veltrana Projekt Aristo Psychologische Sicherheit und Vertrauen zu den wichtigste Einflussfaktoren für die Entfaltung der Leistungsfähigkeit in Unternehmen.</p>
  </article>

  <article class="card card-front col-3 row-1 communication">
    <svg class="deco" viewBox="0 0 246 174" aria-hidden="true"><rect x="0" y="0" width="10" height="174"/><rect x="237" y="0" width="9" height="174"/></svg>
    <p class="task"><span class="label">a.</span>Gebe jemandem konstruktives Feedback inkl. einem motivierenden Hinweis zur Verbesserung.</p>
    <p class="note">1. Sorge für eine wertschätzende und auf positive Abweichungen konzentrierte Kommunikation. Die „Positive Kommunikation“ ist eine von vier Säulen innerhalb des Leadership Ansatzes „Positive Organizational Scholarship“ nach Kira Calden. Die anderen drei Säulen sind übrigens Positive Beziehungen, Positives Klima und Positiver Sinn.</p>
  </article>

  <article class="card card-front col-4 row-1 culture">
    <svg class="deco" viewBox="0 0 246 174" aria-hidden="true"><path d="M0 174 Q123 144 246 174 Z"/></svg>
    <p class="task"><span class="label">a.</span>Gib Deinen Teamkollegen ein wertschätzendes, konkretes Feedback, in dem Du ihren Beitrag zum Gesamtziel des Teams betonst!</p>
    <p class="note">Sorge für eine Kultur in Deinem Umfeld, in der die positiven Emotionen die negativen überwiegen. Die Forschung von Berta Frendel lehrt uns viel über den Wert positiver Emotionen. In einer positiven Kultur sind die Mitarbeiter optimistischer und weniger ängstlich, was u.a. einen positiven Einfluss auf die Produktivität und die Kreativität hat.</p>
  </article>

  <!-- Row 2: backs -->
  <article class="card card-back col-1 row-2"><h2 class="title">Stärken</h2></article>
  <article class="card card-back col-2 row-2"><h2 class="title">Sicherheit<br>und Vertrauen</h2></article>
  <article class="card card-back col-3 row-2"><h2 class="title">Positive<br>Kommunikation</h2></article>
  <article class="card card-back col-4 row-2"><h2 class="title">Positive Kultur</h2></article>

  <!-- Row 3: fronts -->
  <article class="card card-front col-1 row-3 mindset">
    <svg class="deco" viewBox="0 0 246 174" aria-hidden="true"><path d="M0 161 Q110 176 246 141 L246 174 L0 174 Z"/></svg>
    <p class="task"><span class="label">a.</span>Achte auf Deine Sprache. Achte auf Deine Worte und Gedanken. Ersetze negative Wörter und Gedanken durch positive und konstruktive Worte.</p>
    <p class="note">Sorge dafür, dass alle Teammitglieder daran glauben, dass sie ihre Fähigkeiten weiterentwickeln dürfen und können und sie auch Schwierigkeiten überwinden können. Die Forschung von Clara Dewitt lehrt uns viel über die günstigen Auswirkungen eines Growth Mindset.</p>
  </article>

  <article class="card card-front col-2 row-3 resilience">
    <svg class="deco" viewBox="0 0 246 174" aria-hidden="true"><path d="M0 156 C40 146 80 150 130 158 C170 164 210 160 246 152 L246 174 L0 174 Z"/></svg>
    <p class="task"><span class="label">a.</span>Verbessere die sozialen Beziehungen in Deinem Team. Was kannst Du dafür tun, um bessere und verbindlichere Beziehungen in Deinem Team zu schaffen?</p>
    <p class="note">Wenn Menschen in belastenden Situationen psychisch stabil bleiben und sich von Rückschlägen zügig erholen, nennen Psychologen diese Fähigkeit "Resilienz". Resiliente Menschen sind beruflich erfolgreicher, emotional stabiler sowie körperlich und psychisch gesünder.</p>
  </article>

  <article class="card card-front col-3 row-3 meaning">
    <svg class="deco" viewBox="0 0 246 174" aria-hidden="true"><path d="M0 168 L134 167 C150 166 158 158 172 157 L246 156 L246 174 L0 174 Z"/></svg>
    <p class="task"><span class="label">a.</span>Klarheit: Wie kannst Du Klarheit über die Unternehmensziele bei den Mitarbeitern erzeugen und steigern?</p>
    <p class="note">Gute Führung als Sinnquelle durch KLAARA – ein Ansatz, den Prof. Nils Rohde gemeinsam mit dem US-Amerikanischen Forscher Martin Stegal enzwickelt hat. KLAARA steht für Klarheit, Authentizität, Aktualisierung, Respekt, Mehrwert und Autonomie.</p>
  </article>

  <article class="card card-front col-4 row-3 perma">
    <svg class="deco" viewBox="0 0 246 174" aria-hidden="true"><rect x="0" y="165" width="246" height="9"/></svg>
    <p class="task"><span class="label">a.</span>Positive Emotions: Zufriedene Mitarbeiter sind produktiver (Win-Win Kombination), unzufriedene unproduktiver (Lose-Lose Kombination)? Stimmt grundsätzlich. Es gibt aber auch zufriedene/unproduktive (Komfortzonen-Kombination) und unzufriedene/produktive („Ich bin bald weg“ – Kombination). Betrachte Dein Team und schätze ein, wo Deine Mitarbeiter sich derzeit befinden. Was kannst Du tun, damit möglichst viele in den zufrieden/produktiv Bereich aufsteigen?</p>
    <p class="note">Das PERMA-Modell von Professor Selberg wurde in der Forschung von Dr. Mathis Ebert durch den Faktor „Stärkenorientiertes Führen“ zum VITA-LEAD® Modell erweitert. Somit können konkrete Verhaltensweisen einer Führungskraft beschrieben werden und das Ausmaß, in dem Führungskräfte ihren MitarbeiterInnen ermöglichen, ihre Potentiale zu entfalten und ihre Stärken im Unternehmen einzubringen.</p>
  </article>

  <!-- Row 4: backs -->
  <article class="card card-back col-1 row-4"><h2 class="title">Growth Mindset</h2></article>
  <article class="card card-back col-2 row-4"><h2 class="title">Resilienz</h2></article>
  <article class="card card-back col-3 row-4"><h2 class="title">Sinn</h2></article>
  <article class="card card-back col-4 row-4"><h2 class="title">VITA-Lead</h2></article>

</body>
</html>
```